Simple menu needed for Asian food truck

We are an Asian food truck that attends big festivals. Our menu is very simple featuring only about 5 or 6 dishes, but we need big pictures and lettering to capture the attention of festival goers. Our motto is "Fresh, Authentic, Homemade", it would be great to include that somewhere. We also need a menu that possibly magnetic so that we can easily take off items that are sold out, change pricing or add different dishes for specific venues. Attached is an example of what our current menu looks like.

```html
<!DOCTYPE html>
<html lang="en">
<head>
<meta charset="utf-8">
<title>Mei's Street Kitchen – Festival Menu</title>
<link href="https://fonts.googleapis.com/css2?family=Montserrat:wght@400;500;700;800;900&family=Allura&display=swap" rel="stylesheet">
<style>
  :root{
    --bg:#dcdcdc;
    --board:#000000;
    --orange:#e07a0c;
    --white:#ffffff;
    --rule:#5a5a5a;
    --dots:#8a8a8a;
  }
  *{margin:0;padding:0;box-sizing:border-box}
  html,body{width:1200px;height:2236px;overflow:hidden;background:var(--bg)}
  body{font-family:'Montserrat',sans-serif;color:var(--white)}
  .menu{position:absolute;left:50px;top:340px;width:1100px;height:1556px;background:var(--board);overflow:hidden;box-shadow:0 6px 18px rgba(0,0,0,.25)}
  .hero-art{position:absolute;left:0;top:0;width:1100px;height:560px}
  .brand{position:absolute;left:76px;top:64px;width:192px;height:192px;border-radius:50%;background:var(--white);display:flex;align-items:center;justify-content:center;text-align:center}
  .brand-name{font-weight:800;color:var(--orange);font-size:25px;line-height:1.15;letter-spacing:.5px}
  .motto{position:absolute;left:78px;top:272px;line-height:1}
  .motto-fresh{display:block;font-weight:900;font-size:100px;color:var(--orange);letter-spacing:1px}
  .motto-authentic{display:block;font-weight:900;font-size:86px;color:var(--white);margin-top:-6px;letter-spacing:1px}
  .motto-homemade{display:block;font-family:'Allura',cursive;font-size:138px;color:var(--white);margin-top:-18px;margin-left:-4px}
  .divider{position:absolute;left:80px;top:578px;width:608px;height:2px;background:var(--rule)}
  .divider::before{content:"";position:absolute;left:48px;top:-4px;width:118px;height:9px;border-radius:5px;background:var(--orange)}
  .thumb-band{position:absolute;left:73px;top:608px;width:173px;height:640px}
  .thumb{position:absolute;left:102px;width:114px;height:114px;border-radius:50%;border:4px solid var(--white)}
  .dish-row{position:absolute;left:269px;width:760px;height:84px;display:flex;align-items:center}
  .dish-name{position:relative;font-weight:700;font-size:36px;line-height:1.1;letter-spacing:1px;text-transform:uppercase;white-space:nowrap}
  .dish-name.wrap{white-space:normal;width:410px}
  .dish-note{position:absolute;left:0;top:100%;margin-top:2px;font-weight:400;font-size:20px;letter-spacing:.5px;text-transform:none;white-space:nowrap}
  .leader{flex:1;border-bottom:2px dotted var(--dots);margin:0 10px}
  .qty{font-weight:500;font-size:32px;margin-right:10px}
  .qty.small{font-size:22px;margin-right:6px}
  .price{font-weight:800;font-size:84px;color:var(--orange);line-height:1}
  .tea-cups{position:absolute;left:88px;top:1265px;width:310px;height:92px}
  .tea-row{left:410px;width:619px}
  .footer{position:absolute;left:88px;top:1422px;height:36px;display:flex;align-items:center;white-space:nowrap}
  .payments{display:flex;gap:4px;margin-right:52px}
  .card{width:52px;height:32px;border-radius:3px}
  .pay-name{font-size:30px;font-weight:400}
  .web{font-size:23px;font-weight:500}
  .web::before{content:"|";margin:0 14px 0 16px}
</style>
</head>
<body>
<main class="menu">
  <svg class="hero-art" viewBox="0 0 1100 560">
    <defs>
      <radialGradient id="riceGrad" cx="50%" cy="45%" r="60%">
        <stop offset="0" stop-color="#efe6d2"/>
        <stop offset=".7" stop-color="#d9c9a6"/>
        <stop offset="1" stop-color="#7f9d8c"/>
      </radialGradient>
    </defs>
    <path d="M620 0 L1100 0 L1100 520 L1010 545 L940 500 L850 535 L760 470 L700 400 L640 330 L575 260 L610 190 L560 120 L600 60 Z" fill="var(--orange)"/>
    <ellipse cx="880" cy="215" rx="300" ry="175" transform="rotate(-24 880 215)" fill="url(#riceGrad)" role="img" aria-label="Photo of vegetable fried rice on a sage green plate"/>
  </svg>

  <div class="brand"><span class="brand-name">Mei's<br>Street<br>Kitchen</span></div>

  <h1 class="motto">
    <span class="motto-fresh">FRESH</span>
    <span class="motto-authentic">AUTHENTIC</span>
    <span class="motto-homemade">Homemade</span>
  </h1>
  <div class="divider"></div>

  <svg class="thumb-band" viewBox="0 0 173 640" aria-hidden="true">
    <path d="M20 20 L150 0 L173 110 L140 220 L170 330 L135 440 L165 560 L100 630 L10 610 L25 480 L0 360 L25 240 L0 120 Z" fill="var(--orange)"/>
  </svg>
  <div class="thumb" role="img" aria-label="Photo of chicken egg rolls" style="top:615px;background:radial-gradient(circle,#c9944e,#e8dccb)"></div>
  <div class="thumb" role="img" aria-label="Photo of fresh spring rolls" style="top:733px;background:radial-gradient(circle,#6fa34a,#f1ede2)"></div>
  <div class="thumb" role="img" aria-label="Photo of BBQ pork skewers" style="top:865px;background:radial-gradient(circle,#8a4a26,#eadfce)"></div>
  <div class="thumb" role="img" aria-label="Photo of fried rice" style="top:995px;background:radial-gradient(circle,#e6d6b4,#f3efe6)"></div>
  <div class="thumb" role="img" aria-label="Photo of stuffed chicken wings" style="top:1122px;background:radial-gradient(circle,#9c4f22,#e7dccb)"></div>

  <div class="dish-row" style="top:627px">
    <span class="dish-name">Chicken Eggrolls</span><span class="leader"></span><span class="qty">3 for</span><span class="price">$6</span>
  </div>
  <div class="dish-row" style="top:742px">
    <span class="dish-name">Fresh Springrolls<span class="dish-note">(Shrimp or Veggie)</span></span><span class="leader"></span><span class="qty">2 for</span><span class="price">$6</span>
  </div>
  <div class="dish-row" style="top:894px">
    <span class="dish-name wrap">Chinese BBQ Pork Skewers</span><span class="leader"></span><span class="qty">2 for</span><span class="price">$6</span>
  </div>
  <div class="dish-row" style="top:1008px">
    <span class="dish-name">Fried Rice<span class="dish-note">(Chicken or Pork)</span></span><span class="leader"></span><span class="qty">Bowl</span><span class="price">$5</span>
  </div>
  <div class="dish-row" style="top:1121px">
    <span class="dish-name">Angel Wing<span class="dish-note">(Stuffed Chicken Wing) with side of fried rice</span></span><span class="leader"></span><span class="qty small">Combo</span><span class="price">$6</span>
  </div>

  <svg class="tea-cups" viewBox="0 0 310 92" role="img" aria-label="Photos of three cups of flavored tea">
    <circle cx="49" cy="46" r="44" fill="#e9e2c8" stroke="#fff" stroke-width="4"/>
    <circle cx="154" cy="46" r="44" fill="#c8261c" stroke="#fff" stroke-width="4"/>
    <circle cx="253" cy="46" r="44" fill="#e3cc98" stroke="#fff" stroke-width="4"/>
  </svg>
  <div class="dish-row tea-row" style="top:1267px">
    <span class="dish-name">Flavored Tea<span class="dish-note">Strawberry, Mango, or Peach</span></span><span class="leader"></span><span class="price">$5</span>
  </div>

  <div class="footer">
    <div class="payments" aria-label="Accepted payment cards">
      <span class="card" style="background:#f4f4f4"></span>
      <span class="card" style="background:#e57c22"></span>
      <span class="card" style="background:#3a8fd0"></span>
      <span class="card" style="background:#f0e6dc"></span>
    </div>
    <span class="pay-name">Bramblepay</span>
    <span class="web">www.meistreetkitchen.com/menu</span>
  </div>
</main>
</body>
</html>
```